Refresh of a rather uncommon tech outfit website

Our web site is starting to show it's age. You can see the existing site here: www.plumfarrow.net. As a growing company we want to come across as a dynamic collection of IT experts.

We want to update the design so are open to any colour palette and look, but want to retain our current table logo. We use the logo on our business cards but with a white background - see the attached file, so you don't need to keep the brown or the green.

The design should consider the range of browsers that will be looking at the site - so please show how it will look on a wide screen laptop and a 768x1024 tablet.

We want to add some pages about our team and their skills, probably with photos of each person on the team.

This is an uncoded project - the PSD files of the design is required, not coding.
Updates

Thanks everyone for the submissions so far.  It's a holiday day in the UK today but we will get some feedback on the designs so far out to you.

Target Market(s)

Architects and other creative types looking for IT support

Industry/Entity Type

Business

Font styles to use
Serif
Sans Serif

Requirements
Must have
• Must look good on a laptop and an Zelva.

```html
<!DOCTYPE html>
<html lang="en">
<head>
<meta charset="utf-8">
<title>plumfarrow – Serious IT Support for Business</title>
<link href="https://fonts.googleapis.com/css2?family=Open+Sans:wght@400;600;700&family=Oswald:wght@400;500;600&display=swap" rel="stylesheet">
<style>
:root{
  --plum:#8e1a56;
  --plum-dark:#5e0f38;
  --gold:#e9b20e;
  --ink:#2a2a2a;
  --muted:#6b6b6b;
  --line:#dcdcdc;
  --dark:#1c1c1c;
  --footer:#2d2d2d;
  --footer-text:#bdbdbd;
  --white:#ffffff;
}
*{box-sizing:border-box;margin:0;padding:0}
html,body{width:1200px;height:2553px;overflow:hidden;background:var(--white)}
body{font-family:"Open Sans",Arial,sans-serif;color:var(--ink);position:relative}
.abs{position:absolute}
.page{position:relative;width:1200px;height:2553px;overflow:hidden}

/* header */
.brand{left:89px;top:26px;display:flex;align-items:center;gap:12px;font-size:30px;font-weight:700;color:var(--ink);letter-spacing:-.5px}
.brand-mark{width:30px;height:30px;background:var(--gold)}
.remote{right:110px;top:34px;display:flex;align-items:center;gap:10px;font-size:15px;font-weight:600}
.remote-input{width:132px;height:26px;border:1px solid var(--line);font-size:12px;color:#aaa;padding:4px 8px;font-family:inherit}
.remote-go{width:28px;height:26px;background:var(--gold);display:flex;align-items:center;justify-content:center}
.nav{left:0;top:92px;width:1200px;height:41px;background:var(--gold)}
.nav ul{list-style:none;display:flex;position:absolute;left:107px;top:7px;gap:0}
.nav li{font-size:16px;font-weight:600;color:var(--white);padding:2px 10px;text-transform:uppercase;line-height:24px;margin-right:12px}
.nav li.active{background:var(--plum)}

/* hero */
.hero{left:0;top:133px;width:1200px;height:459px;background:linear-gradient(100deg,#7d1550 0%,#a42b6a 45%,#8a1a55 100%)}
.hero-title{left:0;top:338px;width:1200px;text-align:center;font-family:"Oswald",sans-serif;font-size:34px;letter-spacing:9px;color:var(--white);font-weight:500}
.hero-title span{color:var(--gold)}
.hero-arrow{top:320px}

/* services */
.services-photo{left:0;top:592px;width:740px;height:715px;background:radial-gradient(circle at 55% 50%,#e8e6e2 0%,#f4f2ef 45%,#ffffff 75%)}
.services-banner{left:0;top:868px;width:383px;height:179px;background:var(--gold);clip-path:polygon(0 0,92% 0,100% 50%,92% 100%,0 100%)}
.services-banner p{position:absolute;left:18px;top:18px;font-family:"Oswald",sans-serif;font-size:40px;line-height:46px;color:var(--white);font-weight:500}
.service-rail{left:644px;top:684px;width:3px;height:515px;background:var(--gold)}
.service{left:616px;width:500px;height:110px}
.service-icon{position:absolute;left:0;top:-8px;width:60px;height:60px;border-radius:50%;background:var(--white);border:3px solid var(--gold);display:flex;align-items:center;justify-content:center}
.service h3{position:absolute;left:86px;top:0;font-size:14px;font-weight:700;text-transform:uppercase}
.service p{position:absolute;left:86px;top:22px;width:330px;font-size:12.5px;line-height:21px;color:var(--muted)}

/* what we do */
.offer{left:0;top:1307px;width:1200px;height:488px;background:linear-gradient(180deg,#202020,#151515)}
.offer h2{position:absolute;top:64px;width:1200px;text-align:center;font-size:26px;font-weight:600;color:var(--white);letter-spacing:1px}
.offer-intro{position:absolute;left:190px;top:118px;width:820px;text-align:center;font-size:13px;line-height:25px;color:#d6d6d6}
.offer-item{top:1562px;width:180px;text-align:center}
.offer-circle{width:144px;height:144px;border-radius:50%;border:2px solid #cfcfcf;margin:0 auto;display:flex;align-items:center;justify-content:center}
.offer-item.active .offer-circle{background:var(--plum);border-color:var(--plum)}
.offer-label{margin-top:12px;font-size:17px;font-weight:600;color:var(--white)}
.offer-item.active .offer-label{color:var(--gold)}

/* news & clients */
.section-title{font-size:26px;font-weight:700;text-transform:uppercase;color:var(--ink);letter-spacing:.3px}
.news-item{left:89px;width:480px;height:80px}
.news-date{position:absolute;left:0;top:0;width:64px;height:64px;border:1px solid var(--line);text-align:center;padding-top:4px}
.news-date b{display:block;font-size:24px;line-height:30px;font-weight:600}
.news-date span{font-size:11px;color:var(--muted);text-transform:uppercase}
.news-item h4{position:absolute;left:90px;top:0;font-size:13px;font-weight:700}
.news-item p{position:absolute;left:90px;top:24px;width:400px;font-size:12.5px;line-height:22px;color:var(--muted)}
.news-item p em{color:var(--plum);font-style:normal}
.news-rule{left:89px;width:480px;height:1px;background:var(--line)}
.client{width:148px;height:64px;display:flex;align-items:center;justify-content:center;font-size:15px;font-weight:600;text-align:center;line-height:18px}
.client.light{border:1px solid var(--line);color:#9a9a9a}
.client.dark{background:#151515;color:var(--white)}
.client.plum{background:#27306b;color:var(--white)}

/* footer */
.footer{left:0;top:2247px;width:1200px;height:306px;background:var(--footer);color:var(--footer-text)}
.footer h5{position:absolute;top:33px;font-size:13px;font-weight:700;color:var(--white);text-transform:uppercase}
.footer-links{position:absolute;top:64px;list-style:none;font-size:12px;line-height:22px}
.footer-contact{position:absolute;left:300px;top:64px;width:230px;text-align:center;font-size:12px;line-height:18px}
.footer-contact strong{color:var(--white)}
.blog-post{position:absolute;left:567px;width:300px;height:46px}
.blog-post b{position:absolute;left:0;top:0;font-size:20px;font-weight:600;color:#9a9a9a;line-height:22px}
.blog-post small{position:absolute;left:0;top:22px;font-size:10px;text-transform:uppercase}
.blog-post p{position:absolute;left:40px;top:0;width:230px;font-size:11.5px;line-height:17px}
.newsletter{position:absolute;left:911px;top:64px;width:200px}
.newsletter p{font-size:11.5px;line-height:17px}
.newsletter-input{margin-top:14px;width:200px;height:34px;background:var(--white);color:var(--ink);font-size:12px;padding:9px 10px}
.newsletter-btn{margin-top:14px;width:120px;height:38px;background:var(--gold);color:var(--white);font-weight:700;font-size:14px;text-align:center;line-height:38px}
.copyright{position:absolute;left:89px;top:258px;font-size:11.5px;color:#cfcfcf}
.social{position:absolute;right:90px;top:248px;display:flex;align-items:center;gap:7px;font-size:15px;color:var(--white)}
.social i{display:block;width:30px;height:30px}
</style>
</head>
<body>
<div class="page">

  <header>
    <div class="abs brand"><span class="brand-mark"></span>plumfarrow</div>
    <div class="abs remote">Remote
      <div class="remote-input">Session ID</div>
      <div class="remote-go"><svg width="12" height="12" viewBox="0 0 12 12"><path d="M4 2l4 4-4 4" stroke="#fff" stroke-width="2" fill="none"/></svg></div>
    </div>
  </header>

  <nav class="abs nav">
    <ul>
      <li class="active">Home</li><li>About</li><li>What we do</li><li>Team</li><li>Support</li><li>News blog</li><li>Clients</li><li>Articles</li><li>Partners</li><li>Contact us</li>
    </ul>
  </nav>

  <section>
    <div class="abs hero" role="img" aria-label="Support team working at headsets in an office, tinted plum"></div>
    <svg class="abs hero-arrow" style="left:58px" width="44" height="84" viewBox="0 0 44 84"><path d="M40 2L4 42l36 40" stroke="#fff" stroke-width="2" fill="none"/></svg>
    <svg class="abs hero-arrow" style="left:1098px" width="44" height="84" viewBox="0 0 44 84"><path d="M4 2l36 40L4 82" stroke="#fff" stroke-width="2" fill="none"/></svg>
    <h1 class="abs hero-title">SERIOUS IT SUPPORT <span>FOR BUSINESS</span></h1>
  </section>

  <section>
    <div class="abs services-photo" role="img" aria-label="Hand holding a white keyboard key marked help"></div>
    <div class="abs services-banner"><p>SERIOUS<br>IT SUPPORT<br>FOR BUSINESS</p></div>
    <div class="abs service-rail"></div>

    <div class="abs service" style="top:684px">
      <div class="service-icon"><svg width="28" height="28" viewBox="0 0 28 28"><circle cx="14" cy="14" r="9" fill="none" stroke="#8e1a56" stroke-width="4" stroke-dasharray="4 3"/><circle cx="14" cy="14" r="4" fill="#8e1a56"/></svg></div>
      <h3>IT Support &amp; Management</h3>
      <p>Client / Server Networks Cabling and Wireless Solutions Data and Voice Convergence Security &amp; Penetration Testing Multi-site Connectivity.</p>
    </div>
    <div class="abs service" style="top:804px">
      <div class="service-icon"><svg width="30" height="22" viewBox="0 0 30 22"><path d="M7 20a6 6 0 010-12 8 8 0 0115-2 6 6 0 011 14z" fill="#8e1a56"/></svg></div>
      <h3>Cloud Computing</h3>
      <p>Customer Control Panel Manges Resources Increase Performance and Availability Unlimited Bandwidth/Unlimited Storage Geographic Seperation for Failover Transfer of Risk &amp; Reduced TCO.</p>
    </div>
    <div class="abs service" style="top:924px">
      <div class="service-icon"><svg width="28" height="28" viewBox="0 0 28 28"><path d="M14 3a11 11 0 1011 11" stroke="#8e1a56" stroke-width="4" fill="none"/><path d="M20 2l6 6-7 2z" fill="#8e1a56"/></svg></div>
      <h3>Disaster Recovery</h3>
      <p>Defined RPO and RTO Objectives Enterprise Class Recoverability Mirrored Off-site Servers/Data Rapid Deployment of Failover Infrastructure Low Incremental Costs.</p>
    </div>
    <div class="abs service" style="top:1047px">
      <div class="service-icon"><svg width="28" height="28" viewBox="0 0 28 28"><rect x="3" y="3" width="10" height="10" fill="#8e1a56" transform="rotate(45 8 8)"/><rect x="15" y="15" width="10" height="10" fill="#8e1a56" transform="rotate(45 20 20)"/></svg></div>
      <h3>Virtualisation</h3>
      <p>Server &amp; Storage Virtualisation High Availability Server Nodes Application Streaming Secure Remote Desktops Tellan &amp; Hovera Deployments.</p>
    </div>
    <div class="abs service" style="top:1164px">
      <div class="service-icon"><svg width="24" height="28" viewBox="0 0 24 28"><rect x="2" y="2" width="20" height="24" fill="none" stroke="#8e1a56" stroke-width="3"/><path d="M7 20l5-12 5 12" stroke="#8e1a56" stroke-width="3" fill="none"/></svg></div>
      <h3>CAD Services</h3>
      <p>Brackwell Product Customisation CAD Management BIM for Designers Ferncad Modeller Consultancy Training and Implementation.</p>
    </div>
  </section>

  <section class="abs offer" role="region" aria-label="What we can do for you">
    <h2>WHAT WE CAN DO FOR YOU</h2>
    <p class="offer-intro">plumfarrow offer a wide range of services tailored to meet our client's business needs. We aim to deliver world-class support and strategic advice backed up by an effective on-site presence. Our core business is focused on construction professionals and creative companies with sophisticated and fast-changing IT requirements</p>
  </section>

  <div class="abs offer-item active" style="left:86px">
    <div class="offer-circle"><svg width="60" height="60" viewBox="0 0 60 60"><circle cx="30" cy="30" r="26" fill="none" stroke="#fff" stroke-width="4"/><circle cx="30" cy="30" r="5" fill="#fff"/><path d="M30 22l-8-14a26 26 0 0116 0zM37 34l16 0a26 26 0 01-8 14zM23 34l-8 14a26 26 0 01-8-14z" fill="#fff"/></svg></div>
    <div class="offer-label">Support</div>
  </div>
  <div class="abs offer-item" style="left:301px">
    <div class="offer-circle"><svg width="56" height="60" viewBox="0 0 56 60"><circle cx="28" cy="18" r="13" fill="none" stroke="#fff" stroke-width="5"/><path d="M5 56c0-14 10-22 23-22s23 8 23 22z" fill="none" stroke="#fff" stroke-width="5"/></svg></div>
    <div class="offer-label">Consultancy</div>
  </div>
  <div class="abs offer-item" style="left:513px">
    <div class="offer-circle"><svg width="60" height="52" viewBox="0 0 60 52" fill="#fff"><rect x="0" y="0" width="18" height="10"/><rect x="21" y="0" width="18" height="10"/><rect x="42" y="0" width="18" height="10"/><rect x="0" y="14" width="28" height="10"/><rect x="32" y="14" width="28" height="10"/><rect x="0" y="28" width="18" height="10"/><rect x="21" y="28" width="18" height="10"/><rect x="42" y="28" width="18" height="10"/><rect x="0" y="42" width="28" height="10"/><rect x="32" y="42" width="28" height="10"/></svg></div>
    <div class="offer-label">CAD</div>
  </div>
  <div class="abs offer-item" style="left:727px">
    <div class="offer-circle"><svg width="50" height="60" viewBox="0 0 50 60" fill="#fff"><ellipse cx="25" cy="8" rx="24" ry="7"/><path d="M1 14c4 8 44 8 48 0v12c-4 8-44 8-48 0zM1 32c4 8 44 8 48 0v12c-4 8-44 8-48 0zM1 50c4 8 44 8 48 0v2c0 6-48 6-48 0z"/></svg></div>
    <div class="offer-label">Hosting</div>
  </div>
  <div class="abs offer-item" style="left:941px">
    <div class="offer-circle"><svg width="56" height="56" viewBox="0 0 56 56"><path d="M8 48L36 20" stroke="#fff" stroke-width="8" stroke-linecap="round"/><circle cx="40" cy="16" r="11" fill="none" stroke="#fff" stroke-width="5"/><path d="M10 8l38 40" stroke="#fff" stroke-width="6" stroke-linecap="round"/></svg></div>
    <div class="offer-label">Development</div>
  </div>

  <section>
    <h2 class="abs section-title" style="left:89px;top:1858px">Latest News &amp; Blogs</h2>

    <article class="abs news-item" style="top:1924px">
      <div class="news-date"><b>11</b><span>Apr</span></div>
      <h4>plumfarrow Vessa and Korrin App launched</h4>
      <p>plumfarrow have released Vessa and Korrin apps that allow customers to submit and track support requests on their smart <em>[...]</em></p>
    </article>
    <div class="abs news-rule" style="top:2004px"></div>
    <article class="abs news-item" style="top:2026px">
      <div class="news-date"><b>18</b><span>Apr</span></div>
      <h4>Quillstone Certified Installation Engineers</h4>
      <p>plumfarrow are resellers of Quillstone's StoraTune and StoraChord products. These products allow you to convert commodity server <em>[...]</em></p>
    </article>
    <div class="abs news-rule" style="top:2106px"></div>
    <article class="abs news-item" style="top:2118px">
      <div class="news-date"><b>20</b><span>Apr</span></div>
      <h4>plumfarrow Vessa and Korrin App launched</h4>
      <p>plumfarrow have released Vessa and Korrin apps that allow customers to submit and track support requests on their smart <em>[...]</em></p>
    </article>

    <h2 class="abs section-title" style="left:613px;top:1858px">Our Client &amp; Partner</h2>
    <div class="abs client plum" style="left:613px;top:1927px">Orrin Partners</div>
    <div class="abs client dark" style="left:787px;top:1927px">Marla Pendrick</div>
    <div class="abs client light" style="left:962px;top:1927px">Velm &amp; Co</div>
    <div class="abs client light" style="left:613px;top:2022px;color:var(--ink)">Haskett Bray</div>
    <div class="abs client light" style="left:787px;top:2022px;color:var(--gold)">Nolt Studio</div>
    <div class="abs client light" style="left:962px;top:2022px">Ashby Lowe</div>
    <div class="abs client light" style="left:613px;top:2114px">Fenwick Architects</div>
    <div class="abs client light" style="left:787px;top:2114px;color:var(--ink)">Grainline</div>
    <div class="abs client light" style="left:962px;top:2114px;color:#3a7fb8">Outline</div>
  </section>

  <footer class="abs footer">
    <h5 style="left:89px">Quick Links</h5>
    <ul class="footer-links" style="left:89px"><li>Home</li><li>About</li><li>What we do</li><li>Team</li><li>Support</li></ul>
    <ul class="footer-links" style="left:205px"><li>News blog</li><li>Clients</li><li>Articles</li><li>Partners</li><li>Contact</li></ul>

    <h5 style="left:372px">Get in Touch</h5>
    <div class="footer-contact">Call: 020 7946 0381<br>Email: hello@plumfarrow.net<br>Fax: 020 7946 0382<br><strong>or</strong><br><strong>Address:</strong><br>Larch House, 48 Harrow Lane<br>London EC2V 9QT, United Kingdom</div>

    <h5 style="left:567px">Latest Blog Posts</h5>
    <div class="blog-post" style="top:64px"><b>20</b><small>Apr</small><p>Vestibulum ac lorem ut enim faucibus scelerisque sit sed leo.</p></div>
    <div class="blog-post" style="top:120px"><b>11</b><small>Apr</small><p>Quisque condimentum eros ut nisi commodo sed fermentum magna faucibus.</p></div>
    <div class="blog-post" style="top:176px"><b>10</b><small>Apr</small><p>Integer dapibus faucibus leo, sed tempus justo aliquet sit amet.</p></div>

    <h5 style="left:911px">Newsletter</h5>
    <div class="newsletter">
      <p>Enter your email id and get update news &amp; Offer!</p>
      <div class="newsletter-input">Email_id</div>
      <div class="newsletter-btn">SUBMIT</div>
    </div>

    <p class="copyright">© Copyright 2014 plumfarrow. All rights reserved.</p>
    <div class="social">Stay Connected:
      <i style="background:#3b5b9a" aria-label="Social link 1"></i>
      <i style="background:#3fa3d8" aria-label="Social link 2"></i>
      <i style="background:#2f7cb3" aria-label="Social link 3"></i>
      <i style="background:#d34a36" aria-label="Social link 4"></i>
    </div>
  </footer>

</div>
</body>
</html>
```